Moving comapny Postcard mailer Design

I am looking for a 6x9 postcard with real images of our team. I would like to add the same review we currently have , I want the colors of the postcard to be orange and white. I want the team picture to be enlarged with the other pictures to be mimized. I will add example postcards to give rough ideas. My company is called Harlow Moving and the postcards with that name are our current postcards. The additional postcards are from other companies who have better postcards than mine. My goal is for my postcard to be better that theirs.

Target Market(s)

Wealthy people in the 35+ age group

Industry/Entity Type

Moving company

Requirements
Must have
• Beauty

```html
<!DOCTYPE html>
<html lang="en">
<head>
<meta charset="utf-8">
<title>Harlow Moving – Postcard Mailer</title>
<link href="https://fonts.googleapis.com/css2?family=Oswald:wght@500;700&family=Open+Sans:ital,wght@0,400;0,600;0,700;1,400&family=Kaushan+Script&display=swap" rel="stylesheet">
<style>
:root{
  --bg:#2b2d31;
  --blue:#1e56b0;
  --blue-dark:#153a7c;
  --navy:#14284f;
  --orange:#f26a1b;
  --orange-deep:#e0560c;
  --yellow:#ffc21a;
  --white:#ffffff;
  --ink:#1b1b1b;
  --photo-a:#7d8a96;
  --photo-b:#a8967e;
}
*{box-sizing:border-box;margin:0;padding:0}
html,body{width:898px;height:1200px;overflow:hidden;background:var(--bg)}
body{position:relative;font-family:"Open Sans",Arial,sans-serif}
.card{position:absolute;left:59px;width:780px;height:520px;background:var(--white);overflow:hidden;box-shadow:0 8px 24px rgba(0,0,0,.45)}
.card--front{top:60px}
.card--back{top:620px}
.col{position:absolute;top:0;bottom:0}
.head{font-family:"Oswald",Impact,sans-serif;font-weight:700;text-transform:uppercase;line-height:.95}
.photo{position:absolute;background:linear-gradient(160deg,var(--photo-a),var(--photo-b))}

/* front */
.front-left{left:0;width:380px;background:var(--blue)}
.brand-title{position:absolute;left:22px;top:14px;color:var(--white);font-size:38px;letter-spacing:1px}
.front-left .photo{left:0;top:100px;width:380px;height:235px}
.call-script{position:absolute;left:22px;top:348px;color:var(--white);font-family:"Kaushan Script",cursive;font-size:30px}
.call-script small{font-family:"Open Sans",sans-serif;font-size:13px;font-weight:600;margin-left:6px}
.phone-big{position:absolute;left:22px;top:392px;color:var(--white);font-family:"Oswald",sans-serif;font-weight:700;font-size:44px;display:flex;align-items:center;gap:12px}
.site{position:absolute;left:22px;top:470px;color:var(--white);font-size:14px;font-weight:600}

.front-right{left:380px;width:400px}
.ask{position:absolute;left:20px;top:18px;color:var(--orange);font-size:40px}
.ask-sub{position:absolute;left:22px;top:105px;color:var(--ink);font-size:13px;font-weight:700}
.ask-lift{position:absolute;left:22px;top:122px;color:var(--orange);font-family:"Oswald",sans-serif;font-weight:700;font-size:19px;text-transform:uppercase}
.brand-chip{position:absolute;right:16px;top:18px;width:118px;height:112px;border:2px solid var(--blue);display:flex;flex-direction:column;align-items:center;justify-content:center;gap:8px;color:var(--blue);font-family:"Oswald",sans-serif;font-weight:700;font-size:16px;text-transform:uppercase;text-align:center;line-height:1}
.brand-chip .dot{width:26px;height:26px;background:var(--orange)}
.review{position:absolute;left:0;top:155px;width:400px;height:230px;background:var(--orange);padding:14px 20px;color:var(--white)}
.stars{display:flex;gap:6px;margin-bottom:8px}
.review p{font-size:12.5px;font-style:italic;line-height:1.45}
.dot-no{margin-top:8px;font-size:11px;font-weight:700}
.coupons{position:absolute;left:0;top:385px;width:400px;height:135px;background:var(--white);display:flex;gap:10px;padding:12px 14px}
.coupon{flex:1;background:var(--navy);border:2px dashed var(--yellow);color:var(--white);text-align:center;font-family:"Oswald",sans-serif;font-weight:700;display:flex;flex-direction:column;justify-content:center}
.coupon .amt{font-size:34px;line-height:1}
.coupon .off{font-size:18px;color:var(--yellow)}
.coupon .min{font-size:22px;border-top:1px solid rgba(255,255,255,.5);margin:4px 12px 0;padding-top:3px}

/* back */
.back-left{left:0;width:390px;background:var(--blue)}
.quote-title{position:absolute;left:22px;top:14px;color:var(--white);font-size:42px}
.quote-call{position:absolute;left:22px;top:58px;color:var(--white);font-family:"Oswald",sans-serif;font-weight:500;font-size:24px}
.quote-phone{position:absolute;left:22px;top:84px;color:var(--white);font-family:"Oswald",sans-serif;font-weight:700;font-size:28px}
.back-left .photo{left:0;top:132px;width:390px;height:210px}
.about{position:absolute;left:22px;right:22px;top:358px;color:var(--white);font-size:13px;line-height:1.55}

.back-right{left:390px;width:390px}
.simple-band{position:absolute;left:0;top:0;width:390px;height:150px;background:var(--orange)}
.simple-title{position:absolute;left:18px;top:16px;color:var(--white);font-size:40px}
.simple-band .brand-chip{top:18px;right:14px;width:112px;height:112px;background:var(--white);border:none}
.creds{position:absolute;left:0;top:150px;width:390px;height:34px;background:var(--white);color:var(--blue-dark);font-size:10px;font-weight:700;text-transform:uppercase;display:flex;align-items:center;justify-content:center;letter-spacing:.3px}
.back-right .photo--one{left:10px;top:186px;width:180px;height:276px}
.back-right .photo--two{left:200px;top:186px;width:180px;height:276px}
.services{position:absolute;left:0;top:470px;width:390px;height:50px;background:var(--white);border-top:4px solid var(--orange);color:var(--blue-dark);font-family:"Oswald",sans-serif;font-weight:700;font-size:14px;text-transform:uppercase;display:flex;align-items:center;justify-content:center;letter-spacing:.5px}
</style>
</head>
<body>

<section class="card card--front">
  <div class="col front-left">
    <h1 class="head brand-title">Harlow<br>Moving</h1>
    <div class="photo" role="img" aria-label="Harlow Moving team photo in front of company trucks"></div>
    <div class="call-script">Call us today<small>to get started!</small></div>
    <div class="phone-big">
      <svg width="30" height="30" viewBox="0 0 24 24" aria-hidden="true"><path fill="#fff" d="M6.6 10.8a15.1 15.1 0 0 0 6.6 6.6l2.2-2.2c.3-.3.7-.4 1-.2 1.1.4 2.3.6 3.6.6.6 0 1 .4 1 1V20c0 .6-.4 1-1 1A17 17 0 0 1 3 4c0-.6.4-1 1-1h3.5c.6 0 1 .4 1 1 0 1.3.2 2.5.6 3.6.1.3 0 .7-.2 1z"/></svg>
      (555) 214-0370
    </div>
    <div class="site">www.harlowmoving.com</div>
  </div>

  <div class="col front-right">
    <h2 class="head ask">Are You<br>Moving?</h2>
    <div class="ask-sub">Let us Handle</div>
    <div class="ask-lift">Heavy Lifting</div>
    <div class="brand-chip"><span class="dot"></span>Harlow<br>Moving</div>
    <div class="review">
      <div class="stars">
        <svg width="130" height="22" viewBox="0 0 130 22" aria-label="five stars" role="img">
          <g fill="#ffc21a">
            <path id="st" d="M11 1l3 6.6 7.2.8-5.4 4.9 1.5 7.1L11 16.8 4.7 20.4l1.5-7.1L.8 8.4 8 7.6z"/>
            <use href="#st" x="27"/><use href="#st" x="54"/><use href="#st" x="81"/><use href="#st" x="108"/>
          </g>
        </svg>
      </div>
      <p>"This company is incredible! After working all day, the crew showed up on time and got right to work, moving every heavy piece with real care. They were friendly, quick and careful with our home. They took great care of everything we own. Thank you for a great experience!"</p>
      <div class="dot-no">DOT # 4827150</div>
    </div>
    <div class="coupons">
      <div class="coupon"><span class="amt">$25</span><span class="off">OFF</span><span class="min">$1000</span></div>
      <div class="coupon"><span class="amt">$50</span><span class="off">OFF</span><span class="min">$1000</span></div>
      <div class="coupon"><span class="amt">$100</span><span class="off">OFF</span><span class="min">$3000</span></div>
    </div>
  </div>
</section>

<section class="card card--back">
  <div class="col back-left">
    <h2 class="head quote-title">Free Quote</h2>
    <div class="quote-call">CALL US TODAY</div>
    <div class="quote-phone">(555) 214-0370</div>
    <div class="photo" role="img" aria-label="Movers carrying boxes out of a truck"></div>
    <p class="about">For over ten years, our team at Harlow Moving has been providing our region with unparalleled custom moving experiences. We prioritize safety, timeliness, and communication to ensure our customers are happy &amp; stress-free before, during, and after their move. No matter where you need to go, we're here to help!</p>
  </div>

  <div class="col back-right">
    <div class="simple-band">
      <h2 class="head simple-title">Moving<br>Made<br>Simple</h2>
      <div class="brand-chip"><span class="dot"></span>Harlow<br>Moving</div>
    </div>
    <div class="creds">Locally owned &amp; operated &nbsp;•&nbsp; Licensed, insured, bonded</div>
    <div class="photo photo--one" role="img" aria-label="Mover wrapping furniture inside a home"></div>
    <div class="photo photo--two" role="img" aria-label="Movers loading wrapped furniture into a truck"></div>
    <div class="services">Residential • Commercial • Long Distance • Packing</div>
  </div>
</section>

</body>
</html>
```